HomePage Design for Lumen Getaways - once-in-a-lifetime experiences for busy working people

Design a homepage for the Lumen Getaways (www.lumengetaways.example) website compatible with further web pages and the design briefing documents attached

LG HomePage Design Brief
We are seeking website HomePage designs incorporating our new Logo and colour scheme, for Lumen Getaways (www.lumengetaways.example) to go with the site functionality and wireframe ideas attached.
The website HomePage design needs to
• Incorporate and be consistent with the LG Logo and its colour scheme attached.
• Express the brand values of being inspirational, high quality, upscale, cultured, aspirational, and contemporary – even somewhat ‘hip’. Probably positioned somewhere between Harlow Pike (Deluxe Travel) and Green Walrus (Hip Travel) – see https://www.harlowpike.example and https://www.greenwalrus.example .
• Be instantly recognisable and different from other travel websites and instantly communicate the nature of the brand proposition and target customer base.
• Appeal to our core 25-55 affluent businesspeople demographic
• Work in the UK, US/Canada and Australia/NZ and ultimately in mainland Europe.
• Use fonts and colours that are easily reproduced online and compatible with nearly all browsers.
• Be part of a responsive website design, that can be used both on Desktops and laptops but also with tablets and mobile ‘phones (hence content not too wide across the page)
• Feature the strapline ‘Lumen Getaways in less than 7 Days’
• Work with the and wireframes and processes shown in the attached presentation – although intended as a guide only these features and processes all need to be incorporated into the HomePage.
• Make full use of high quality images and video to convey our brand proposition and products

Target Market(s)

25-55 affluent businesspeople

Industry/Entity Type

Travel Industry

Number of Pages Required

1 page

Font styles to use
Sans Serif

Colors
0455a3
00a88f

Requirements
Must have
• • Incorporate and be consistent with the LG Logo and its colour scheme attached.
• • Express the brand values of being inspirational, high quality, upscale, cultured, aspirational, and contemporary – even somewhat ‘hip’. Probably positioned somewhere between Harlow Pike (Deluxe Travel) and Green Walrus (Hip Travel) – see https://www.harlowpike.example and https://www.greenwalrus.example .
• • Be instantly recognisable and different from other travel websites and instantly communicate the nature of the brand proposition and target customer base.
• • Appeal to our core 25-55 affluent businesspeople demographic
• • Be part of a responsive website design, that can be used both on Desktops and laptops but also with tablets and mobile ‘phones (hence content not too wide across the page)
• • Feature the strapline ‘Lumen Getaways in less than 7 Days’
• • Work with the and wireframes and processes shown in the attached presentation – although intended as a guide only these features and processes all need to be incorporated into the HomePage.
• • Make full use of high quality images and video to convey our brand proposition and products
• Colours as per Logo not as shown below
Nice to have
• • Work in the UK, US/Canada and Australia/NZ and ultimately in mainland Europe.
Should not have
• Must not be cheap or mass-market, nor excessively "stuffy or luxury-orientated"

```html
<!DOCTYPE html>
<html lang="en">
<head>
<meta charset="utf-8">
<title>Lumen Getaways — Home</title>
<link href="https://fonts.googleapis.com/css2?family=Cabin:wght@400;500;600&display=swap" rel="stylesheet">
<style>
:root{
  --bar:#333333;
  --paper:#e8e8e8;
  --green:#1f5e2c;
  --green-text:#1e6b2e;
  --navy:#1f2d6b;
  --white:#ffffff;
  --ink:#444444;
}
*{box-sizing:border-box;margin:0;padding:0}
html,body{width:858px;height:1200px;overflow:hidden}
body{position:relative;font-family:"Cabin",sans-serif;background:var(--paper);color:var(--ink)}
.abs{position:absolute}

.top-bar{left:0;top:0;width:858px;height:28px;background:var(--bar);color:var(--white);font-size:11px;letter-spacing:.5px}
.top-bar .phone{left:60px;top:7px}
.top-bar .email{left:0;width:858px;text-align:center;top:7px}
.socials{display:flex;gap:8px}
.socials span{width:17px;height:17px;border-radius:50%;background:var(--white);display:block}
.top-bar .socials{left:688px;top:5px}

.masthead{left:0;top:28px;width:858px;height:104px;background:var(--paper)}
.brand{left:0;width:858px;top:40px;text-align:center;display:flex;justify-content:center;align-items:center;gap:8px}
.brand .dot{width:14px;height:14px;border-radius:50%;background:var(--green-text)}
.brand .name{font-size:20px;font-weight:600;color:var(--green-text);letter-spacing:1px}
.brand-tag{left:0;width:858px;top:68px;text-align:center;font-size:6px;color:var(--green-text);letter-spacing:1.5px;font-weight:600}

.hero{left:0;top:132px;width:858px;height:373px}
.hero-tag{left:524px;top:246px;width:86px;height:22px;background:var(--white);color:#222;font-size:10px;display:flex;align-items:center;justify-content:center}

.main-nav{left:0;top:509px;width:858px;height:41px;background:var(--green);display:flex;align-items:center;padding-left:44px}
.main-nav a{color:var(--white);text-decoration:none;font-size:11px;font-weight:500;padding:0 15px;height:41px;line-height:41px;border-right:1px solid rgba(255,255,255,.15)}
.main-nav a:nth-child(7){border-right:none}
.main-nav .login{margin-left:15px;background:var(--white);color:var(--green-text);border-radius:4px;height:26px;line-height:26px;padding:0 10px;border:none}

.section-title{font-size:15px;font-weight:500;color:var(--green-text);text-align:center;top:571px}
.t-exp{left:0;width:574px}
.t-last{left:591px;width:232px}

.card{width:128px;height:142px;background:var(--white);box-shadow:0 0 3px rgba(0,0,0,.15);text-align:center}
.card .pic{margin:4px auto 0;width:120px;height:60px}
.card h3{font-size:8.5px;font-weight:500;color:var(--green-text);margin-top:9px;line-height:1.1}
.card p{font-size:7px;line-height:1.4;margin:5px 6px 0;color:var(--ink)}
.card .more{position:absolute;left:38px;bottom:10px;width:52px;height:11px;background:var(--navy);color:var(--white);font-size:6.5px;line-height:11px}

.place{left:591px;width:210px;height:99px}
.place .cap{position:absolute;left:0;bottom:0;width:100%;height:16px;background:rgba(0,0,0,.55);color:var(--white);font-size:8.5px;font-weight:500;text-align:center;line-height:16px}

.site-footer{left:0;top:924px;width:858px;height:126px;background:var(--green);color:var(--white);font-size:10.5px}
.site-footer ul{list-style:none;position:absolute;top:31px;line-height:17.3px}

.partners{left:0;top:1050px;width:858px;height:115px;background:var(--white)}
.partner{top:50px;font-size:15px;font-weight:600;color:#111}

.bottom-bar{left:0;top:1165px;width:858px;height:35px;background:var(--bar);color:var(--white);font-size:11px;font-weight:500;letter-spacing:.3px}
.bottom-bar .legal{left:60px;top:11px}
.bottom-bar .socials{left:688px;top:9px}
</style>
</head>
<body>

<header class="top-bar abs">
  <span class="phone abs">020-7946-0321</span>
  <span class="email abs">info@lumengetaways.example</span>
  <div class="socials abs"><span></span><span></span><span></span><span></span><span></span></div>
</header>

<div class="masthead abs">
  <div class="brand abs"><span class="dot"></span><span class="name">LUMEN GETAWAYS</span></div>
  <div class="brand-tag abs">IN LESS THAN 7 DAYS</div>
</div>

<section class="hero abs">
  <svg width="858" height="373" viewBox="0 0 858 373">
    <defs>
      <linearGradient id="gBalloonL" x1="0" y1="0" x2="0" y2="1"><stop offset="0" stop-color="#7fb6e0"/><stop offset=".6" stop-color="#5b8cb3"/><stop offset="1" stop-color="#3f6b2e"/></linearGradient>
      <linearGradient id="gMarble" x1="0" y1="0" x2="0" y2="1"><stop offset="0" stop-color="#6fa6e0"/><stop offset=".35" stop-color="#dcdcdc"/><stop offset="1" stop-color="#bdb8b0"/></linearGradient>
      <linearGradient id="gStatue" x1="0" y1="0" x2="0" y2="1"><stop offset="0" stop-color="#8fc0ec"/><stop offset=".5" stop-color="#b7a184"/><stop offset="1" stop-color="#5a4d42"/></linearGradient>
      <linearGradient id="gGold" x1="0" y1="0" x2="0" y2="1"><stop offset="0" stop-color="#9ec8f0"/><stop offset=".45" stop-color="#d4a52a"/><stop offset="1" stop-color="#6d7f8a"/></linearGradient>
      <linearGradient id="gBalloonR" x1="0" y1="0" x2="0" y2="1"><stop offset="0" stop-color="#e98a3a"/><stop offset=".5" stop-color="#8fb4d8"/><stop offset="1" stop-color="#4c7a38"/></linearGradient>
    </defs>
    <polygon points="0,0 46,0 156,373 0,373" fill="url(#gBalloonL)" role="img" aria-label="Hot air balloon over green hills"/>
    <polygon points="46,0 272,0 384,373 156,373" fill="url(#gMarble)" role="img" aria-label="White marble domed mausoleum"/>
    <polygon points="272,0 500,0 608,373 384,373" fill="url(#gStatue)" role="img" aria-label="Large seated stone statue at a temple"/>
    <polygon points="500,0 724,0 836,373 608,373" fill="url(#gGold)" role="img" aria-label="Golden temple reflected in water"/>
    <polygon points="724,0 858,0 858,373 836,373" fill="url(#gBalloonR)" role="img" aria-label="Hot air balloons above mountains"/>
    <g stroke="#ffffff" stroke-width="3">
      <line x1="46" y1="0" x2="156" y2="373"/><line x1="272" y1="0" x2="384" y2="373"/>
      <line x1="500" y1="0" x2="608" y2="373"/><line x1="724" y1="0" x2="836" y2="373"/>
    </g>
  </svg>
  <div class="hero-tag abs">Vlogs &amp; Reviews</div>
</section>

<nav class="main-nav abs">
  <a>Destinations</a><a>Experiences</a><a>Trips by Month</a><a>Topical Now</a><a>Tailored</a><a>Pioneers Club</a><a>Vlogs &amp; Reviews</a><a class="login">CLIENT LOG-IN</a>
</nav>

<h2 class="section-title t-exp abs">LUMEN GETAWAYS IN LESS THAN 7 DAYS!</h2>
<h2 class="section-title t-last abs">LAST FEW PLACES</h2>

<article class="card abs" style="left:55px;top:598px"><div class="pic" style="background:linear-gradient(#9aa6b0,#8a7a5a)" role="img" aria-label="Elephants on a savanna"></div><h3>Wonders of Wildlife</h3><p>Lorem Ipsum is simply dummy text printing and typesetting industry</p><span class="more">Read More</span></article>
<article class="card abs" style="left:189px;top:598px"><div class="pic" style="background:linear-gradient(#d43a3a,#e06a9a)" role="img" aria-label="Festival crowd under stage lights"></div><h3>Experiences</h3><p>Lorem Ipsum is simply dummy text printing and typesetting industry</p><span class="more">Read More</span></article>
<article class="card abs" style="left:323px;top:598px"><div class="pic" style="background:linear-gradient(#a8b4b8,#6a5440)" role="img" aria-label="Brown bear roaring"></div><h3>Must Do Activities</h3><p>Lorem Ipsum is simply dummy text printing and typesetting industry</p><span class="more">Read More</span></article>
<article class="card abs" style="left:457px;top:598px"><div class="pic" style="background:linear-gradient(#3a3a6a,#c86a5a)" role="img" aria-label="Hot air balloon at dusk"></div><h3>Unique Annual Events</h3><p>Lorem Ipsum is simply dummy text printing and typesetting industry</p><span class="more">Read More</span></article>

<article class="card abs" style="left:128px;top:760px"><div class="pic" style="background:linear-gradient(#7aa0c8,#4f7a2e)" role="img" aria-label="Green mountain ridges"></div><h3>Extraordinary &amp; Secret Places</h3><p>Lorem Ipsum is simply dummy text printing and typesetting industry</p><span class="more">Read More</span></article>
<article class="card abs" style="left:262px;top:760px"><div class="pic" style="background:linear-gradient(#0a1a3a,#1a2a5a)" role="img" aria-label="Dancers leaping on a dark stage"></div><h3>Unforgettable Performances</h3><p>Lorem Ipsum is simply dummy text printing and typesetting industry</p><span class="more">Read More</span></article>
<article class="card abs" style="left:396px;top:760px"><div class="pic" style="background:linear-gradient(#b8c0c4,#7a7a72)" role="img" aria-label="Climber on a rocky peak"></div><h3>Spectacular Hiking,<br>Climbing &amp; Walking</h3><p style="margin-top:3px">Lorem Ipsum is simply dummy text printing and typesetting industry</p><span class="more">Read More</span></article>

<div class="place abs" style="top:599px;background:linear-gradient(#9ab4cc,#6a4a8a)" role="img" aria-label="Masked carnival costume by a lagoon"><span class="cap">Venice Carnival £599pp</span></div>
<div class="place abs" style="top:701px;background:linear-gradient(#8aa0a8,#5a6a3a)" role="img" aria-label="Stone statue on a grassy hillside"><span class="cap">Easter Island £2,999pp</span></div>
<div class="place abs" style="top:802px;background:linear-gradient(#5a3a2a,#2a1a1a)" role="img" aria-label="Festival celebrants in costume"><span class="cap">Day of the Dead £3,299pp</span></div>

<footer class="site-footer abs">
  <ul style="left:60px"><li>About Us</li><li>Our Partners</li><li>Newsletter</li><li>FAQs</li></ul>
  <ul style="left:177px"><li>Contact Us</li><li>Booking Conditions</li><li>Privacy &amp; Cookies</li><li>Terms of Use</li></ul>
  <ul style="left:320px"><li>Financial Protection</li><li>Travel</li><li>Visas</li><li>Travel Advice</li></ul>
  <ul style="left:470px"><li>Group booking</li><li>Tailor-Made &amp; Extra Nights</li><li>Booking Fights</li><li>Careers with LG</li></ul>
  <ul style="left:642px"><li>LG Protecting eildlife &amp; animals,</li><li>and Supporting local communities</li><li>Prsss Room</li></ul>
</footer>

<section class="partners abs">
  <span class="partner abs" style="left:60px">Harlow Pike</span>
  <span class="partner abs" style="left:196px">Green Walrus</span>
  <span class="partner abs" style="left:332px">Harlow Pike</span>
  <span class="partner abs" style="left:468px">Green Walrus</span>
  <span class="partner abs" style="left:612px">Harlow Pike</span>
  <span class="partner abs" style="left:748px">Green Walrus</span>
</section>

<div class="bottom-bar abs">
  <span class="legal abs">Privacy policy - Legal mentions - Terms and Conditions</span>
  <div class="socials abs"><span></span><span></span><span></span><span></span><span></span></div>
</div>

</body>
</html>
```